" Eu ajudo pequenos e médios empresários a desenvolver suas habilidades empreendedoras e as de suas equipes, de maneira a alavancar os resultados da empresa. "

```html
<!DOCTYPE html>
<html lang="pt-BR">
<head>
<meta charset="utf-8">
<title>Rafael Monteiro — Coach dos Empresários</title>
<link href="https://fonts.googleapis.com/css2?family=Open+Sans:wght@400;600;700&family=Roboto+Condensed:wght@400;700&display=swap" rel="stylesheet">
<style>
  :root{
    --navy:#0f2236;
    --gold:#c9a23a;
    --ink:#1d2a38;
    --text:#3c4652;
    --paper:#ffffff;
    --soft:#eef0f2;
    --line:#b9bec4;
  }
  *{box-sizing:border-box;margin:0;padding:0}
  html,body{width:1200px;height:1200px;overflow:hidden;background:var(--paper)}
  body{font-family:"Open Sans",Arial,sans-serif;color:var(--text);position:relative}
  .page{position:absolute;left:300px;top:0;width:600px;height:1195px;background:var(--paper)}
  .abs{position:absolute}

  .topbar{left:0;top:0;width:600px;height:29px;background:var(--navy)}
  .nav{left:22px;top:0;height:29px;display:flex;gap:18px;align-items:center;font-family:"Roboto Condensed",sans-serif;font-weight:700;font-size:10px;color:#fff;letter-spacing:.3px}
  .social{left:396px;top:4px;display:flex;gap:6px}
  .social span{width:30px;height:30px;border-radius:50%;display:block;border:2px solid #fff}

  .hero{left:0;top:29px;width:600px;height:351px;background:linear-gradient(100deg,#e6e9ec 0%,#d5dbe1 45%,#b9c3cd 100%)}
  .brand-panel{left:17px;top:12px;width:206px;height:132px;background:var(--navy);display:flex;flex-direction:column;align-items:center;justify-content:center}
  .brand-mark{width:30px;height:30px;background:var(--gold);margin-bottom:10px}
  .brand-name{font-family:"Roboto Condensed",sans-serif;font-weight:700;font-size:20px;color:#fff;letter-spacing:.5px;line-height:1;white-space:nowrap}
  .brand-tag{font-family:"Roboto Condensed",sans-serif;font-weight:700;font-size:8px;color:#fff;letter-spacing:1.5px;margin-top:6px;white-space:nowrap}
  .signup{left:17px;top:152px;width:206px;font-size:8px;color:var(--ink)}
  .signup p{text-align:center;margin-bottom:8px}
  .signup label{display:block;font-size:8px;margin-top:4px}
  .field{display:block;height:13px;background:#fff;border:1px solid var(--line)}
  .btn{display:block;margin:8px auto 0;width:52px;height:15px;background:var(--gold);color:var(--navy);font-family:"Roboto Condensed",sans-serif;font-weight:700;font-size:8px;text-align:center;line-height:15px}
  .hero-title{left:34px;top:278px;font-family:"Roboto Condensed",sans-serif;font-weight:700;font-size:21px;line-height:1.2;color:var(--ink)}
  .hero-photo{left:312px;top:0;width:228px;height:351px;background:linear-gradient(180deg,#c3ccd5 0%,#5b6675 55%,#1e2733 100%)}
  .hero-band{left:0;top:380px;width:600px;height:18px;background:var(--navy)}

  .heading{display:flex;gap:6px;align-items:flex-start}
  .heading i{width:5px;height:26px;background:var(--gold);display:block;flex:none}
  .heading h2{font-family:"Roboto Condensed",sans-serif;font-weight:700;font-size:11.5px;line-height:1.15;color:var(--ink);text-transform:uppercase}
  .rule{height:1px;background:var(--line)}

  .photo{background:linear-gradient(135deg,#d9d2c6,#8c7d6a)}
  .small{font-size:6.5px;line-height:1.45;color:var(--text)}
  .small p{margin-bottom:6px}
  .case-text{font-size:5.6px;line-height:1.45}

  .list{list-style:none;font-size:7px;line-height:1.3;color:var(--text)}
  .list li{margin-bottom:7.5px}
  .list li::before{content:"• ";color:var(--ink)}

  .contact{left:24px;top:1030px;width:552px;height:136px;background:var(--soft)}
  .contact-lead{font-family:"Roboto Condensed",sans-serif;font-size:13px;color:var(--ink);line-height:1.3}
  .form-row{display:flex;align-items:center;justify-content:flex-end;gap:6px;font-size:7px;color:var(--ink);margin-bottom:5px}
  .form-row .field{width:185px}
  .footer{left:0;top:1170px;width:600px;height:24px;background:var(--navy);color:#fff;font-size:6.5px;display:flex;align-items:center;padding-left:28px;gap:14px}
</style>
</head>
<body>
<div class="page">

  <div class="abs topbar"></div>
  <nav class="abs nav"><span>PRINCIPAL</span><span>QUEM SOU</span><span>SERVIÇOS</span><span>CONTATO</span></nav>
  <div class="abs social" aria-label="Redes sociais">
    <span style="background:#3b5998"></span>
    <span style="background:#3a3a3a"></span>
    <span style="background:#0e76a8"></span>
    <span style="background:#1da1f2"></span>
    <span style="background:#d0302a"></span>
  </div>

  <section class="abs hero">
    <div class="abs brand-panel">
      <div class="brand-mark"></div>
      <div class="brand-name">RAFAEL MONTEIRO</div>
      <div class="brand-tag">COACH DOS EMPRESÁRIOS</div>
    </div>
    <form class="abs signup">
      <p>Receba dicas grátis diretamente no seu email</p>
      <label>Nome</label><span class="field"></span>
      <label>E-mail</label><span class="field"></span>
      <span class="btn">ENVIAR</span>
    </form>
    <div class="abs hero-photo" role="img" aria-label="Foto do coach de terno, braços cruzados"></div>
    <h1 class="abs hero-title">Coaching, Consultoria e<br>Inteligência Emocional</h1>
  </section>
  <div class="abs hero-band"></div>

  <div class="abs heading" style="left:30px;top:418px;width:260px"><i></i><h2>O segredo para ir mais longe<br>e mais depressa</h2></div>
  <div class="abs photo" style="left:30px;top:452px;width:235px;height:136px" role="img" aria-label="Foto de reunião de empresários em escritório"></div>

  <div class="abs heading" style="left:313px;top:418px;width:270px"><i></i><h2>Case de sucesso:<br>nome da empresa ou do empresário</h2></div>
  <div class="abs small case-text" style="left:313px;top:452px;width:58px">
    <p>Conheça a trajetória de um cliente que dobrou o faturamento em um ano.</p>
    <p>Com metas claras e rotina de acompanhamento, os resultados vieram antes.</p>
    <p>Hoje a empresa cresce com líderes preparados e processos simples.</p>
  </div>
  <div class="abs photo" style="left:377px;top:452px;width:200px;height:136px;background:linear-gradient(135deg,#cbb79a,#6d5a45)" role="img" aria-label="Foto de empresária em sua loja"></div>

  <div class="abs rule" style="left:30px;top:602px;width:548px"></div>
  <div class="abs heading" style="left:30px;top:610px"><i style="height:16px"></i><h2>Quem sou</h2></div>
  <div class="abs small" style="left:30px;top:636px;width:330px">
    <p>Sou coach de empresários e ajudo pequenos e médios negócios a desenvolver habilidades empreendedoras nas pessoas e nas equipes. Há mais de dez anos acompanho donos de empresas que querem crescer com método, foco e clareza de propósito, sem perder o equilíbrio entre vida pessoal e trabalho.</p>
    <p>Meu trabalho une coaching, consultoria e inteligência emocional para transformar a forma como você lidera, decide e se comunica com o time.</p>
    <p>Atendo empresários de diversos setores, em sessões presenciais e online, sempre com planos de ação práticos e indicadores que mostram a evolução de cada etapa do processo.</p>
    <p>Cada encontro é pensado para gerar clareza, compromisso e resultados que você pode medir.</p>
  </div>
  <div class="abs" style="left:377px;top:636px;width:200px;height:120px;background:linear-gradient(90deg,#e9ecef,#b5bec8)" role="img" aria-label="Foto do coach de terno">
    <span class="abs" style="left:22px;top:52px;font-family:'Roboto Condensed',sans-serif;font-weight:700;font-size:12px;color:var(--ink)">SUA FOTO</span>
  </div>
  <div class="abs small" style="left:30px;top:764px;width:548px">
    <p>Minha formação reúne experiência em gestão de empresas, liderança de equipes comerciais e certificação internacional em coaching. Ao longo da carreira, acompanhei centenas de profissionais em momentos de expansão, crise e sucessão, sempre com foco em desenvolvimento humano e resultados concretos para o negócio.</p>
    <p>Acredito que empresas crescem quando seus líderes crescem. Por isso, cada processo começa com um diagnóstico cuidadoso e segue com encontros regulares, tarefas práticas e avaliação contínua dos avanços conquistados por você e sua equipe.</p>
  </div>

  <div class="abs rule" style="left:30px;top:836px;width:548px"></div>
  <div class="abs heading" style="left:30px;top:844px"><i style="height:16px"></i><h2>Serviços</h2></div>
  <div class="abs photo" style="left:30px;top:874px;width:205px;height:134px;background:linear-gradient(135deg,#d8d6d2,#7e7a74)" role="img" aria-label="Foto de empresário em escritório industrial"></div>
  <ul class="abs list" style="left:248px;top:876px;width:330px">
    <li>Coaching individual para empresários</li>
    <li>Desenvolvimento de líderes e equipes</li>
    <li>Consultoria em gestão e processos</li>
    <li>Planejamento estratégico com metas claras</li>
    <li>Inteligência emocional nos negócios</li>
    <li>Treinamentos in company sob medida</li>
    <li>Palestras e workshops para equipes</li>
    <li>Acompanhamento mensal de resultados</li>
  </ul>

  <section class="abs contact">
    <div class="abs heading" style="left:8px;top:8px"><i style="height:16px"></i><h2>Contato</h2></div>
    <div class="abs rule" style="left:8px;top:30px;width:200px"></div>
    <p class="abs contact-lead" style="left:8px;top:38px;width:200px">Interessado em alavancar seus negócios?</p>
    <p class="abs contact-lead" style="left:8px;top:76px;width:200px">Preencha o formulário de contato e envie suas dúvidas!</p>
    <div class="abs" style="left:250px;top:12px;width:290px">
      <div class="form-row">Nome completo: <span class="field"></span></div>
      <div class="form-row">E-mail: <span class="field"></span></div>
      <div class="form-row">Assunto: <span class="field"></span></div>
      <div class="form-row">Mensagem: <span class="field" style="height:26px"></span></div>
    </div>
    <span class="abs btn" style="left:288px;top:118px;margin:0">ENVIAR</span>
    <div class="abs" style="left:430px;top:98px;display:flex;flex-direction:column;align-items:center">
      <div style="width:14px;height:14px;background:var(--gold);margin-bottom:3px"></div>
      <div style="font-family:'Roboto Condensed',sans-serif;font-weight:700;font-size:11px;color:var(--ink);line-height:1;white-space:nowrap">RAFAEL MONTEIRO</div>
    </div>
  </section>

  <footer class="abs footer">
    <span>Contato</span><span>Telefone (00) 0000-0000</span><span>WhatsApp (00) 90000-0000</span><span>E-mail contato@rafaelmonteiro.com.br</span>
  </footer>
</div>
</body>
</html>
```